Snapnook needs You

Help us create an inviting, amazing, sleek, simple, clear landing page for a picture-memory-social connection site!

Business Name: SnapNook
Industry: Social Networking and Creativity through Pictures
A web platform for and about a community that is driven by a passion for sharing, caring, bonding, collaborating, creating and earning with pictures, through pictures and other related creative activities. This is going to be a great site for all creative artists-photographers, artists, graphic artists to express their work and their creativity.

The main focus of the site is - CONNECTIONS.
This will be uncoded.

Desired Website Screen Size
1024x768... Widescreen/Landscape orientation, is what we mean... So it fits on a CPU screen.

Desired look and feel and message
Look: Visitor should feel immersed in the page, in the world the page creates, simple, elegant, sophisticated, contemporary. We really like a clean uncluttered look.

Special mention: By the way we love the marketing genius who thought up this branding for velu yogurt where they used the two dots above the o to create a branding effect that made this brand instantly identifiable. http://www.velu-dairy.ca/en/

The two dots by themselves without having even the name present brings up the whole brand now. The dots are used above all the ingredients of the yogurt creating friendly figures, and above people in commercials-bringing the people onto the side of "team" velu. Snapnook may have a character created or something distinctive in the letters in the name created to brand the site as well.

Feel: Engaging; Magical without being corny, here is a link to give an example look and feel but please do not be hindered in your creativity by this suggestion. We love all creative angles.
http://artscrapheap.com/graphic/5820317-camera-film-roll-blue-background

Message: Life and memories and connections through pictures.

Target audience:
The site is focused on pictures but not confined to photography enthusiasts (although they are an integral part of the site). Customers/Visitors will include families, corporates and the younger generation - all age groups, all class, everyone with pictures to express, memories to share.

Website design we like:
http://morvantstudio.com/work/northern-ballet-guild/
http://morvantstudio.com/work/pixelhop/

What colors do we want to see on our landing page?
We would like the background to be grey or blue since it is grey is picture neutral colour and blue highlights pictures well and we also like blue and silver, which can be integrated into the theme. Also like green. But please do not let these instructions limit your creativity. We are open to new ideas and colours.

Predetermined Concepts if any:
We have a concept in mind and we think it would be cool to have an interface for the user through the back of a camera on the landing page -This could be used to create a scene or world the visitor feels a part of or is immersed into. The back screen of the camera may act as a screen for the slideshow of featured pictures on the site.

Content on the Page:
Photo Gallery with full screen, thumbnail view, zoom option etc.
Prominent but short introductory message
Sign in / Login Options
Links: Home Page; About; Info/Help; Contact Us; Privacy Policy; Terms of Use
At the bottom of the page: Follow Me/Like/Workfolio...social buttons.

Please feel free to add any other element to the landing page that you think might add to the effect of simple yet amazing look -clean, simple, uncluttered, sophisticated, stylish, inviting and engaging.
The concept is a guideline, but we would like you to be as creative as you can, even if it meant stepping out of these guidelines - rethink design, style, content if you like. We believe in bringing a solution in an innovative yet simple and elegant style. Something a visitor would be intrigued enough to explore and the guest would feel comfortable enough taking that step forward to have fun on the site. If you believe in the same, and you have the skill then you will have what we need. Good luck, go for it and we are excited to see what the amazing designers on this amazing site have to offer.
If you have any questions please free to ask.
Updates

HI wanted to send an update that this project design has been guaranteed.

Our site will be one to celebrate and showcase imagination as well as connection.  We would love to see what you create. Keep in mind our site will showcase all creativity, photographs, artists, graphic artists so this would be a benefit you may want to take advantage of in the future, a place where, if you so choose, you could gain exposure for your work. Therefore, even if you do not win the design project there is possible future benefit.

Imagination is everything.
Imagination encircles the world.-Harwood

Reason: We are giving the designers who accepted invites but have not yet submitted a chance to finish their submissions and the ones who are working on revisions a chance to finish those:)

Hello everyone,

Due to time constraints we must come to a decision sooner than the deadline of 28th. 

So, please try to submit any new designs or modifications to the old ones before the 26th. We are very thankful to all of you who have participated - for your designs, enthusiasm and kind words. 

Good luck! :)

• Thank you for the interest shown and your submissions! Designers who have submitted up until now have shown great potential. We are VERY excited with the quality of work and designs.

We want to add that Snapnook is not exclusively for the photographers. The site is for every person who may have a picture to store, organise, use or share - whether publicly or with only a few friends and family.

Snapnook is about allowing people to take control of their creativity. It is about providing tools to our users so that they can build their own connections and social network... of friends, family, fans, clients, ideas, thoughts, emotions etc. through pictures without worrying about their privacy or control over their creations.

With this update we want to encourage others to go beyond the camera theme. Do not let us restrict your creativity. Let YOUR OWN ideas take over if that’s what you think will best convey the message and will appeal to the users.

```html
<!DOCTYPE html>
<html lang="en">
<head>
<meta charset="utf-8">
<title>Snapnook</title>
<link rel="stylesheet" href="https://fonts.googleapis.com/css2?family=Fredoka:wght@600&family=Acme&family=Open+Sans:wght@400;600;800&display=swap">
<style>
:root{
  --header:#3d3d3d;
  --white:#ffffff;
  --ink:#222222;
  --accent-green:#3ed79b;
  --footer:#0a8aee;
  --tile:rgba(110,110,110,.55);
  --tile-border:#5db8f0;
}
*{margin:0;padding:0;box-sizing:border-box}
html,body{width:1200px;height:958px;overflow:hidden}
body{position:relative;font-family:"Open Sans",sans-serif;background:#d9d9d9}
.site-header{position:absolute;left:0;top:0;width:1200px;height:108px;background:var(--header)}
.brand{position:absolute;left:260px;top:24px;font-family:"Fredoka",sans-serif;font-weight:600;font-size:50px;color:var(--white);letter-spacing:1px;line-height:1}
.account{position:absolute;top:6px;left:844px;display:flex;gap:16px;align-items:center;font-size:10px;color:var(--white)}
.account .login{border:1px solid #7fc4f2;background:var(--white);color:#333;border-radius:3px;padding:1px 4px}
.main-nav{position:absolute;top:84px;left:537px;display:flex;gap:19px;font-size:12px;color:var(--white)}
.main-nav a{color:inherit;text-decoration:none;position:relative;padding-bottom:8px}
.main-nav a.current::after{content:"";position:absolute;left:-1px;right:-3px;bottom:-8px;height:3px;background:var(--accent-green)}
.scene{position:absolute;left:0;top:108px;width:1200px;height:776px;
  background:radial-gradient(ellipse at 10% 10%,#c9d98a 0,transparent 35%),
  radial-gradient(ellipse at 45% 25%,#6a6a66 0,transparent 30%),
  radial-gradient(ellipse at 25% 70%,#c7a796 0,transparent 40%),
  radial-gradient(ellipse at 85% 80%,#8a9a5a 0,transparent 40%),
  linear-gradient(135deg,#b9c98d,#d8d2cb 50%,#8f9572)}
.hero-veil{position:absolute;left:0;top:108px;width:1200px;height:552px;background:rgba(255,255,255,.45)}
.slide-screen{position:absolute;left:341px;top:276px;width:232px;height:181px;border-radius:18px;
  background:radial-gradient(circle at 50% 40%,#5fc4ee,#17679e 60%,#0b3b66);box-shadow:0 0 8px rgba(0,0,0,.35)}
.slider-arrow{position:absolute;top:307px;width:28px;height:60px}
.slider-arrow.prev{left:236px}
.slider-arrow.next{left:956px}
.tagline{position:absolute;left:656px;top:240px;color:var(--ink);font-family:"Acme",sans-serif;line-height:1}
.tagline .l1{font-size:50px;display:block;height:64px}
.tagline .l2{font-size:44px;display:block;height:62px}
.tagline .l3{font-size:50px;font-style:italic;display:block;height:66px}
.tagline .l4{font-family:"Open Sans",sans-serif;font-size:27px;display:block}
.upload{position:absolute;left:491px;top:530px;width:213px;height:95px;border:1px solid #3fa0e0;
  background:linear-gradient(135deg,#4db6f3,#17c3d6 45%,#0a7fb0);box-shadow:3px 3px 5px rgba(0,0,0,.35);
  color:var(--white);font-weight:800;font-size:27px;line-height:32px;text-align:center;padding-top:15px;letter-spacing:.5px}
.feature{position:absolute;top:719px;width:176px;height:105px;background:var(--tile);border:2px solid var(--tile-border);border-radius:2px;
  color:var(--white);text-align:center;font-size:16px;line-height:18px}
.feature svg{display:block;margin:18px auto 6px}
.f1{left:258px}.f2{left:509px}.f3{left:750px}
.site-footer{position:absolute;left:0;top:884px;width:1200px;height:74px;background:var(--footer);color:var(--white)}
.copyright{position:absolute;left:258px;top:41px;font-size:10px}
.follow{position:absolute;left:838px;top:12px;font-size:12px}
.social{position:absolute;left:838px;top:36px;display:flex;gap:9px}
.social span{width:15px;height:15px;border-radius:3px;background:rgba(255,255,255,.85)}
</style>
</head>
<body>
<header class="site-header">
  <div class="brand">snapnook</div>
  <div class="account"><span class="login">Login</span><span>Sign up</span></div>
  <nav class="main-nav"><a class="current">Home</a><a>About</a><a>Info</a><a>Contact Us</a><a>Privacy Policy</a><a>Terms of Use</a></nav>
</header>

<div class="scene" role="img" aria-label="Blurred photo of hands holding a camera seen from behind, green garden background"></div>
<div class="hero-veil"></div>

<div class="slide-screen" role="img" aria-label="Featured picture on the camera screen: film reel on a glowing blue background"></div>
<svg class="slider-arrow prev" viewBox="0 0 28 60"><polygon points="26,0 16,0 2,30 16,60 26,60 12,30" fill="var(--accent-green)"/></svg>
<svg class="slider-arrow next" viewBox="0 0 28 60"><polygon points="2,0 12,0 26,30 12,60 2,60 16,30" fill="var(--accent-green)"/></svg>

<div class="tagline">
  <span class="l1">Life</span>
  <span class="l2">Memories</span>
  <span class="l3">Connections</span>
  <span class="l4">through pictures</span>
</div>

<div class="upload">UPLOAD<br>YOURS</div>

<div class="feature f1">
  <svg width="34" height="30" viewBox="0 0 34 30"><rect x="2" y="6" width="30" height="22" fill="none" stroke="#fff" stroke-width="3"/><polyline points="2,6 17,1 32,6" fill="none" stroke="#fff" stroke-width="2"/><polygon points="5,25 13,14 19,21 23,17 29,25" fill="#fff"/></svg>
  Photo Gallery<br>with full screen
</div>
<div class="feature f2">
  <svg width="68" height="30" viewBox="0 0 68 30"><g fill="none" stroke="#fff" stroke-width="2"><rect x="5" y="5" width="22" height="20"/><rect x="41" y="5" width="22" height="20"/><path d="M1 8V1h7M24 1h7v7M31 22v7h-7M8 29H1v-7M37 8V1h7M60 1h7v7M67 22v7h-7M44 29h-7v-7"/></g><polygon points="8,22 14,13 18,18 24,22" fill="#fff"/><polygon points="44,22 50,13 54,18 60,22" fill="#fff"/></svg>
  Thumbnail<br>view
</div>
<div class="feature f3">
  <svg width="34" height="28" viewBox="0 0 34 28"><path d="M3 7h8l3-5h8l3 5h6v19H3z" fill="#fff"/><circle cx="19" cy="16" r="6" fill="#777"/><circle cx="19" cy="16" r="3" fill="#fff"/><rect x="5" y="3" width="5" height="3" fill="#fff"/></svg>
  <div style="margin-top:6px">Zoom</div>
</div>

<footer class="site-footer">
  <div class="copyright">snapnook. all rights reserved 2012</div>
  <div class="follow">follow us</div>
  <div class="social"><span></span><span></span><span></span><span></span></div>
</footer>
</body>
</html>
```